FestivaLoom Business Cards

Front
Has logo with a design. Website address (www.festivaloom-demo.com)
Has slogan (celebrate every night)
Has phone number (5559183047)
Should be bold and stands out.

Back
Has details about what we offer.

Events
Search upcoming events
Submit events
Party Image Gallery
View and download HQ party images
Sign up as a contributing event photographer and get paid!
Tickets
Sell your event tickets online for free!
Direct pay
No ticket fee

Target Market(s)

These cards will be handed out in clubs and events to patrons.

Industry/Entity Type

Business

Contact Information for Business Card

Should match or mirror our website in some sort of way. Visit the website to get ideas.

Requirements
Must have
• Must be designed for a 3x3 inch card.

```html
<!DOCTYPE html>
<html lang="en">
<head>
<meta charset="utf-8">
<title>FestivaLoom Business Cards</title>
<link href="https://fonts.googleapis.com/css2?family=Open+Sans:wght@400;600;700&family=Oswald:wght@400;500&display=swap" rel="stylesheet">
<style>
  :root {
    --backdrop: #e1e1df;
    --card: #262626;
    --blue: #1ea8e0;
    --pink: #e0357e;
    --white: #f2f2f2;
    --muted: #d0d0d0;
  }
  * { margin: 0; padding: 0; box-sizing: border-box; }
  html, body { width: 1200px; height: 659px; overflow: hidden; background: var(--backdrop); }
  .stage { position: relative; width: 1200px; height: 659px; }
  .card {
    position: absolute; top: 142px; width: 375px; height: 374px;
    background: var(--card); overflow: hidden;
    font-family: "Open Sans", sans-serif; color: var(--white);
  }
  .card--front { left: 201px; }
  .card--back { left: 623px; }

  .brand { position: absolute; left: 27px; top: 46px; display: flex; align-items: center; gap: 10px; }
  .brand__dot { width: 30px; height: 30px; border-radius: 50%; background: var(--blue); }
  .brand__name { font-family: "Open Sans", sans-serif; font-weight: 600; font-size: 30px; color: var(--blue); letter-spacing: -0.5px; line-height: 1; }
  .slogan { position: absolute; left: 68px; top: 84px; font-size: 10px; letter-spacing: 5.2px; color: var(--muted); }

  .contact { position: absolute; left: 27px; top: 196px; }
  .contact__name { font-weight: 700; font-size: 20px; letter-spacing: 0.5px; }
  .contact__role { font-size: 12px; color: var(--muted); margin-top: 1px; }
  .contact__lines { margin-top: 18px; font-size: 14px; line-height: 18px; color: var(--white); }
  .contact__accent { color: var(--blue); }

  .equalizer {
    position: absolute; left: 0; bottom: 0; width: 100%; height: 33px;
    background: linear-gradient(to bottom, var(--pink) 0%, var(--pink) 35%, var(--blue) 55%, var(--blue) 100%);
    opacity: 0.9;
  }

  .offer { position: absolute; left: 30px; top: 40px; font-family: "Oswald", sans-serif; }
  .offer__title { font-weight: 500; font-size: 17px; color: var(--pink); letter-spacing: 0.5px; margin-bottom: 10px; }
  .offer__list { list-style: none; font-size: 15px; line-height: 22px; font-weight: 400; color: var(--white); }
  .offer__list li::before { content: "»"; margin-right: 7px; }

  .brand-vertical {
    position: absolute; left: 312px; top: 320px; transform-origin: 0 0; transform: rotate(-90deg);
    display: flex; flex-direction: column;
  }
  .brand-vertical__name { font-weight: 600; font-size: 27px; color: var(--blue); line-height: 1; display: flex; align-items: center; gap: 8px; }
  .brand-vertical__dot { width: 26px; height: 26px; border-radius: 50%; background: var(--blue); }
  .brand-vertical__slogan { font-size: 9px; letter-spacing: 4.5px; color: var(--muted); margin-top: 4px; margin-left: 34px; }
</style>
</head>
<body>
<main class="stage">
  <section class="card card--front">
    <div class="brand">
      <span class="brand__dot"></span>
      <span class="brand__name">FestivaLoom</span>
    </div>
    <p class="slogan">celebrate every night</p>
    <div class="contact">
      <p class="contact__name">Dana Whitfield</p>
      <p class="contact__role">Managing Director</p>
      <p class="contact__lines">
        5559183047<br>
        support@festivaloom-demo.com<br>
        www.<span class="contact__accent">festivaloom-demo</span>.com
      </p>
    </div>
    <div class="equalizer" role="img" aria-label="Equalizer bar pattern in pink and blue"></div>
  </section>

  <section class="card card--back">
    <div class="offer">
      <h2 class="offer__title">WE OFFER</h2>
      <ul class="offer__list">
        <li>Events</li>
        <li>Search upcoming events</li>
        <li>Submit events</li>
        <li>Party Image Gallery</li>
        <li>View and download HQ party images</li>
        <li>Sign up as a contributing event</li>
        <li>photographer and get paid!</li>
        <li>Tickets</li>
        <li>Sell your event tickets online for free!</li>
        <li>Direct pay</li>
        <li>No ticket fee</li>
      </ul>
    </div>
    <div class="brand-vertical">
      <span class="brand-vertical__name"><span class="brand-vertical__dot"></span>FestivaLoom</span>
      <span class="brand-vertical__slogan">celebrate every night</span>
    </div>
    <div class="equalizer" role="img" aria-label="Equalizer bar pattern in pink and blue"></div>
  </section>
</main>
</body>
</html>
```